Sports Psychology Business Card Design

Need a catchy and unique business card design for our sport psychology practice. We provide mental performance counseling and consulting to performers from all types of industries with a special emphases on athletes.The name of our practice is "Inner Edge of Excellence" or "IEE" as is indicated in the logo examples submitted in this brief. Also provided were logos with specific sports referenced which represent sources of our clients from those sports.

Target Market(s)

Executives, Professionals (doctors, lawyers, etc.), Athletes, Entertainers and other performers

Contact Information for Business Card

Need to include our logo (logos provided in this brief).

Font styles to use
Other font styles liked:
• Font can be found in logo

Colors
0792cd
34a7d8
85cae6

Requirements
Must have
• Our logo and reference to our provision of mental performance counseling/consulting/coaching
Nice to have
• References to sports that our athletes play as provided in the brief.
Should not have
• This is not a general wellness consulting practice. Our focus is on consulting to improve mental performance.

```html
<!DOCTYPE html>
<html lang="en">
<head>
<meta charset="utf-8">
<title>Inner Edge of Excellence – Business Card</title>
<link rel="stylesheet" href="https://fonts.googleapis.com/css2?family=Montserrat:wght@600;800&family=Quicksand:wght@400;500&display=swap">
<style>
  :root {
    --backdrop: #dfe6ee;
    --card-face: #f1f3f6;
    --ink-dark: #232427;
    --panel-dark: #141517;
    --panel-mid: #2c2d30;
    --brand-blue: #1f4d9c;
    --brand-blue-deep: #133a7e;
    --silver: #d9dde4;
    --text-light: #c9ced8;
    --icon-blue: #2b5aa6;
  }
  html, body {
    margin: 0;
    width: 1200px;
    height: 894px;
    overflow: hidden;
    background: var(--backdrop);
  }
  .canvas {
    position: relative;
    width: 1200px;
    height: 894px;
  }
  .business-card {
    position: absolute;
    left: 100px;
    top: 161px;
    width: 1000px;
    height: 571px;
    border-radius: 44px;
    overflow: hidden;
    background: var(--card-face);
    box-shadow: 0 18px 40px rgba(20, 30, 50, 0.18);
  }
  .card-swoosh {
    position: absolute;
    inset: 0;
    width: 1000px;
    height: 571px;
  }
  .brand-lockup {
    position: absolute;
    left: 38px;
    top: 52px;
    display: flex;
    align-items: center;
    gap: 26px;
  }
  .brand-name {
    display: flex;
    align-items: center;
    gap: 10px;
    font-family: "Montserrat", sans-serif;
    font-weight: 800;
    font-size: 66px;
    line-height: 1;
    letter-spacing: 2px;
    color: var(--ink-dark);
  }
  .brand-dot {
    width: 16px;
    height: 16px;
    border-radius: 50%;
    background: var(--brand-blue);
    align-self: flex-end;
    margin-bottom: 6px;
  }
  .brand-tagline {
    font-family: "Montserrat", sans-serif;
    font-weight: 800;
    font-size: 25px;
    line-height: 1.35;
    letter-spacing: 1.5px;
    text-transform: uppercase;
    color: var(--ink-dark);
  }
  .contact-block {
    position: absolute;
    right: 42px;
    top: 328px;
    text-align: right;
  }
  .person-name {
    font-family: "Montserrat", sans-serif;
    font-weight: 600;
    font-size: 30px;
    letter-spacing: 0.5px;
    color: var(--brand-blue);
    margin: 0;
  }
  .person-role {
    font-family: "Quicksand", sans-serif;
    font-weight: 500;
    font-size: 22px;
    color: var(--text-light);
    margin: 4px 0 34px;
  }
  .contact-list {
    list-style: none;
    margin: 0;
    padding: 0;
  }
  .contact-item {
    display: flex;
    justify-content: flex-end;
    align-items: center;
    gap: 12px;
    font-family: "Quicksand", sans-serif;
    font-weight: 400;
    font-size: 22px;
    color: var(--text-light);
    height: 32px;
  }
  .contact-icon {
    width: 22px;
    height: 22px;
    flex: none;
  }
</style>
</head>
<body>
<main class="canvas">
  <section class="business-card" aria-label="Inner Edge of Excellence business card">
    <svg class="card-swoosh" viewBox="0 0 1000 571" aria-hidden="true">
      <defs>
        <linearGradient id="blueBand" x1="0" y1="1" x2="1" y2="0">
          <stop offset="0" stop-color="#1e4f9e"/>
          <stop offset="1" stop-color="#0f3578"/>
        </linearGradient>
        <linearGradient id="darkPanel" x1="0" y1="0" x2="0" y2="1">
          <stop offset="0" stop-color="#2e2f33"/>
          <stop offset="1" stop-color="#121315"/>
        </linearGradient>
      </defs>
      <path class="swoosh-band" fill="url(#blueBand)"
        d="M 940 0 L 1000 0 L 1000 571 L 330 571 C 296 560 300 520 334 478 C 470 318 700 140 940 0 Z"/>
      <path class="swoosh-edge" fill="var(--silver)"
        d="M 952 0 L 1000 0 L 1000 571 L 452 571 C 424 558 430 508 462 468 C 580 318 770 150 952 0 Z"/>
      <path class="swoosh-panel" fill="url(#darkPanel)"
        d="M 960 0 L 1000 0 L 1000 571 L 466 571 C 440 558 446 510 476 472 C 592 324 778 156 960 0 Z"/>
    </svg>

    <header class="brand-lockup">
      <div class="brand-name"><span>IEE</span><span class="brand-dot"></span></div>
      <div class="brand-tagline">The Inner Edge<br>of Excellence</div>
    </header>

    <div class="contact-block">
      <h1 class="person-name">DANA WHITFIELD</h1>
      <p class="person-role">Mental Performance Consultant</p>
      <ul class="contact-list">
        <li class="contact-item">555-014-2291
          <svg class="contact-icon" viewBox="0 0 22 22" aria-label="Phone">
            <circle cx="11" cy="11" r="10.5" fill="var(--icon-blue)"/>
            <path d="M6 9 Q11 5 16 9 L15 11 L13 10 L9 10 L7 11 Z M7 12 H15 V16 H7 Z" fill="#16181b"/>
          </svg>
        </li>
        <li class="contact-item">dana@theiee.co
          <svg class="contact-icon" viewBox="0 0 22 22" aria-label="Email">
            <circle cx="11" cy="11" r="10.5" fill="var(--icon-blue)"/>
            <rect x="5.5" y="7" width="11" height="8" rx="1" fill="#16181b"/>
            <path d="M6 7.5 L11 11.5 L16 7.5" fill="none" stroke="var(--icon-blue)" stroke-width="1.2"/>
          </svg>
        </li>
        <li class="contact-item">www.theiee.co
          <svg class="contact-icon" viewBox="0 0 22 22" aria-label="Website">
            <circle cx="11" cy="11" r="10.5" fill="var(--icon-blue)"/>
            <circle cx="11" cy="11" r="6" fill="none" stroke="#16181b" stroke-width="1.4"/>
            <path d="M5 11 H17 M11 5 V17" stroke="#16181b" stroke-width="1.2"/>
          </svg>
        </li>
      </ul>
    </div>
  </section>
</main>
</body>
</html>
```